Saddle Down at the Meadow 2018

I need a flyer that can be printed in both 8.5x 11 and 11x17.
I have uploaded the flyer I used last year just to give you an idea of what I need
This event will include craft beer, live music and food trucks.
The silent auction is an important part of the evening.
It is a fundraiser for Willow Crest Therapeutic Riding. (we teach horseback riding to special needs children and adults)
I will also need a tshirt design at some point so I would like the logo to be one that is suitable for a tshirt-the tshirt will be a dark color

Target Market(s)

ages 21-55 male and female
horse lovers

Industry/Entity Type

Horseback Riding

Font styles to use
Serif
Sans Serif

Colors

Designer to choose colors to be used in the design.

Requirements
Must have
• horse image
• similar information listed as on the flyer from last year
• second annual 2018
• information about the silent auction
• mention beer, food trucks, live music
• Wheel and Cask logo, lanternfield brewery logo
• November 3, 2018 6:oo-9:00 pm
• $25 ticket price which includes a flight of beer and an event tshirt
• www.wctrmock.example to purchase tickets
• Bramble Equestrian Center
• 8356 West Pinhollow Drive
• Woodstock, GA 30188
• barn logo
• email listed for more info: wctrmock@mailbox.example
Nice to have
• Please join us for a fundraiser to benefit Willow Crest Therapeutic Riding, a non-profit organization that provides emotional, physical and social benefits for children and adults with special needs.
Should not have
• Mane Ride

```html
<!DOCTYPE html>
<html lang="en">
<head>
<meta charset="utf-8">
<title>Saddle Down at the Meadow 2018 – Flyer</title>
<link href="https://fonts.googleapis.com/css2?family=Montserrat:wght@400;500;600;700;800;900&family=Oswald:wght@500;600;700&display=swap" rel="stylesheet">
<style>
  :root {
    --page-bg: #e4e5e7;
    --lime: #d4d500;
    --royal: #1c3f94;
    --ink: #141414;
    --red: #d3131b;
    --white: #ffffff;
    --gold: #f5c400;
    --seal-ring: #b8b8b8;
    --photo-light: #d9d2c8;
    --photo-mid: #a08c78;
    --photo-dark: #6b4a32;
  }
  * { margin: 0; padding: 0; box-sizing: border-box; }
  html, body { width: 1194px; height: 1200px; overflow: hidden; }
  body { background: var(--page-bg); font-family: "Montserrat", sans-serif; color: var(--ink); }

  .flyer { position: absolute; left: 209px; top: 0; width: 776px; height: 1200px; overflow: hidden; background: var(--lime); }
  .abs { position: absolute; }
  .nowrap { white-space: nowrap; }

  .hero-photo { position: absolute; left: 0; top: 0; width: 776px; height: 720px;
    background: linear-gradient(160deg, var(--photo-light) 0%, #bfb3a4 35%, var(--photo-mid) 55%, var(--photo-dark) 80%, #8e7866 100%); }
  .layer { position: absolute; left: 0; top: 0; }

  .edition { left: 440px; top: 160px; width: 300px; text-align: center; color: var(--white); font-weight: 900; line-height: .86; }
  .edition .big { font-size: 55px; letter-spacing: .3px; }
  .edition .year { display: flex; align-items: center; justify-content: center; gap: 6px; font-size: 42px; font-weight: 800; margin-top: 6px; }
  .edition .year::before, .edition .year::after { content: ""; width: 58px; height: 3px; background: var(--white); }

  .circle { position: absolute; border-radius: 50%; background: var(--white); }
  .intro-circle { left: 28px; top: 481px; width: 268px; height: 268px; border: 1.5px solid var(--royal); }
  .date-circle { left: 482px; top: 497px; width: 232px; height: 232px; border: 1.5px solid var(--royal); }
  .logo-circle { left: 244px; top: 343px; width: 288px; height: 288px; }

  .event-name { left: 268px; top: 408px; width: 240px; text-align: center; font-weight: 800; font-size: 27px; line-height: 1.12; color: var(--red); }

  .intro { left: 36px; top: 527px; width: 252px; text-align: center; font-size: 13.2px; font-weight: 500; line-height: 1.58; white-space: nowrap; }
  .intro strong { color: var(--red); font-weight: 700; font-size: 14.4px; }

  .festival-art { left: 238px; top: 569px; width: 308px; height: 154px; border-radius: 150px 150px 0 0;
    background: radial-gradient(ellipse at 50% 65%, #f2d98c 0%, #ecd190 45%, rgba(236,209,144,0) 72%); }
  .festival-art .truck { position: absolute; left: 82px; top: 62px; width: 160px; height: 87px; border-radius: 8px; background: #9b1b1b; }

  .nov { left: 555px; top: 520px; font-size: 50px; font-weight: 900; letter-spacing: -2px; line-height: 1; }
  .day { left: 554px; top: 540px; font-size: 192px; font-weight: 900; color: var(--royal); line-height: 1; }
  .day-year { left: 637px; top: 646px; background: var(--gold); font-weight: 800; font-size: 18px; line-height: 1.2; padding: 1px 8px; transform: rotate(-6deg); }
  .time { left: 680px; top: 564px; width: 84px; height: 84px; border-radius: 50%; background: var(--royal); color: var(--white);
    display: flex; flex-direction: column; align-items: center; justify-content: center; font-weight: 800; font-size: 15px; line-height: .95; }

  .banner-text { left: 109px; top: 728px; width: 571px; text-align: center; font-family: "Oswald", sans-serif; font-weight: 700;
    font-size: 37px; line-height: 1.2; color: var(--white); letter-spacing: -.5px; white-space: nowrap; }

  .auction-title { left: 0; top: 790px; width: 776px; text-align: center; font-family: "Oswald", sans-serif; font-weight: 700; font-size: 25px; line-height: 1.2; color: var(--red); }
  .auction-items { left: 0; top: 836px; width: 776px; text-align: center; font-family: "Oswald", sans-serif; font-weight: 600; font-size: 21px; line-height: 1.38; }

  .info-box { position: absolute; background: var(--white); border: 1.5px solid var(--royal); text-align: center; }
  .venue { left: 65px; top: 891px; width: 138px; height: 128px; padding-top: 9px; }
  .venue h2 { font-size: 15.5px; font-weight: 800; line-height: 1.1; }
  .venue p { font-size: 11.5px; font-weight: 600; line-height: 1.12; margin-top: 1px; }
  .ticket { left: 574px; top: 891px; width: 138px; height: 128px; padding: 8px 4px 0 24px; }
  .ticket .price { font-size: 34px; font-weight: 900; line-height: 1; }
  .ticket p { font-size: 10.8px; font-weight: 600; line-height: 1.16; text-transform: uppercase; white-space: nowrap; }
  .shirt { left: 526px; top: 920px; width: 68px; height: 88px; background: #1a1a1a; border-radius: 10px 10px 4px 4px; }

  .seal { left: 265px; top: 925px; width: 246px; height: 246px; border: 6px solid var(--seal-ring); display: flex; align-items: center; justify-content: center; text-align: center; }
  .seal span { font-weight: 800; font-size: 21px; line-height: 1.18; width: 170px; }

  .sponsor { left: 35px; width: 200px; text-align: center; font-weight: 800; letter-spacing: -.3px; white-space: nowrap; }
  .sponsor-1 { top: 1069px; font-size: 18px; }
  .sponsor-2 { top: 1120px; display: flex; flex-direction: column; align-items: center; gap: 4px; font-size: 15px; line-height: 1.1; }
  .sponsor-2::before { content: ""; width: 20px; height: 20px; border-radius: 50%; background: var(--red); }

  .contact { left: 518px; width: 254px; text-align: center; white-space: nowrap; }
  .contact .label { font-size: 15px; font-weight: 600; line-height: 1.3; }
  .contact .value { font-size: 16px; font-weight: 800; line-height: 1.3; }
  .contact-1 { top: 1060px; }
  .contact-2 { top: 1124px; }
  .contact-2 .value { font-size: 14.5px; }
</style>
</head>
<body>
<main class="flyer">
  <div class="hero-photo" role="img" aria-label="Photograph of a young rider in a helmet cantering a chestnut horse through bare winter trees"></div>

  <svg class="layer" width="776" height="1200" viewBox="0 0 776 1200" aria-hidden="true">
    <polygon points="0,703 388,590 776,694 776,1200 0,1200" fill="var(--lime)"/>
    <circle cx="48" cy="548" r="9" fill="var(--royal)"/>
    <circle cx="752" cy="556" r="6" fill="var(--royal)"/>
    <line x1="32" y1="1045" x2="263" y2="1045" stroke="var(--royal)" stroke-width="1.2"/>
    <line x1="32" y1="1109" x2="238" y2="1109" stroke="var(--royal)" stroke-width="1.2"/>
    <line x1="510" y1="1045" x2="747" y2="1045" stroke="var(--royal)" stroke-width="1.2"/>
    <line x1="541" y1="1115" x2="747" y2="1115" stroke="var(--royal)" stroke-width="1.2"/>
  </svg>

  <div class="abs edition">
    <div class="big">SECOND</div>
    <div class="big">ANNUAL</div>
    <div class="year">2018</div>
  </div>

  <div class="circle intro-circle"></div>
  <div class="circle date-circle"></div>
  <div class="circle logo-circle"></div>

  <div class="abs event-name">Saddle Down at the Meadow</div>

  <p class="abs intro">Please join us for a<br>fundraiser to benefit<br><strong>Willow Crest<br>Therapeutic Riding,</strong><br>a non-profit organization<br>that provides emotional,<br>physical and social benefits<br>for children and adults<br>with special needs.</p>

  <div class="abs festival-art" role="img" aria-label="Illustration of a red food truck with cutlery, music notes and confetti stars">
    <div class="truck"></div>
  </div>

  <div class="abs nov">NOV.</div>
  <div class="abs day">3</div>
  <div class="abs day-year">2018</div>
  <div class="abs time"><span>6:00</span><span>to</span><span>9:00</span><span>pm</span></div>

  <svg class="layer" width="776" height="1200" viewBox="0 0 776 1200" aria-hidden="true">
    <polygon points="66,750 130,742 130,810 72,842 100,794" fill="var(--ink)"/>
    <polygon points="710,750 646,742 646,810 704,842 676,794" fill="var(--ink)"/>
    <polygon points="130,810 112,800 130,790" fill="#8a8a8a"/>
    <polygon points="646,810 664,800 646,790" fill="#8a8a8a"/>
    <path d="M109,740 Q388,690 680,740 L680,800 Q388,752 109,800 Z" fill="var(--royal)"/>
    <path d="M130,843 Q180,822 226,817" stroke="var(--red)" stroke-width="1.5" fill="none"/>
    <path d="M646,843 Q596,822 550,817" stroke="var(--red)" stroke-width="1.5" fill="none"/>
  </svg>

  <div class="abs banner-text">BEER • FOOD TRUCKS • LIVE MUSIC</div>

  <h2 class="abs auction-title">SILENT AUCTION ITEMS INCLUDE:</h2>
  <div class="abs auction-items">• EMBER DOME GRILL &nbsp;• VACATION RENTALS &nbsp;• HOME DECOR<br>• JEWELRY &amp; MUCH MORE</div>

  <div class="info-box venue">
    <h2>BRAMBLE<br>EQUESTRIAN<br>CENTER</h2>
    <p>8356 WEST<br>PINHOLLOW DRIVE<br>WOODSTOCK,<br>GA 30188</p>
  </div>

  <div class="info-box ticket">
    <div class="price">$25</div>
    <p>Ticket price<br>which includes<br>a flight of<br>beer and an<br>event tshirt.</p>
  </div>
  <div class="abs shirt" role="img" aria-label="Black event t-shirt"></div>

  <div class="circle seal"><span>Willow Crest Therapeutic Riding</span></div>

  <div class="abs sponsor sponsor-1">Wheel and Cask</div>
  <div class="abs sponsor sponsor-2">Lanternfield Brewery</div>

  <div class="abs contact contact-1">
    <div class="label">Purchase tickets at:</div>
    <div class="value">www.wctrmock.example</div>
  </div>
  <div class="abs contact contact-2">
    <div class="label">For more info:</div>
    <div class="value">wctrmock@mailbox.example</div>
  </div>
</main>
</body>
</html>
```